Keystone Ward Security - Trade Show Booth 10x20

I need designs for an upcoming trade show booth. We want something sleek, simple that represents our brand well.

Target Market(s)

property Managers

```html
<!DOCTYPE html>
<html lang="en">
<head>
<meta charset="utf-8">
<title>Keystone Ward Security – Trade Show Backdrop</title>
<link href="https://fonts.googleapis.com/css2?family=Barlow:wght@500;700;800&display=swap" rel="stylesheet">
<style>
  :root {
    --page: #d9d9d9;
    --paper: #efefef;
    --ink: #2b2b2b;
    --night: #111111;
    --steel: #7d7d7d;
    --signal: #e0420f;
    --light-text: #e6e6e6;
  }
  * { margin: 0; padding: 0; box-sizing: border-box; }
  html, body {
    width: 1200px; height: 800px; overflow: hidden;
    background: var(--page);
    font-family: "Barlow", Arial, sans-serif;
  }
  .backdrop {
    position: absolute; left: 20px; top: 113px;
    width: 1160px; height: 574px; overflow: hidden;
    background: linear-gradient(90deg, var(--paper) 0%, var(--paper) 40%, #9a9a9a 62%, #2a2a2a 82%, var(--night) 100%);
  }
  .backdrop-art { position: absolute; inset: 0; }
  .brand-lockup {
    position: absolute; left: 60px; top: 205px; width: 430px;
    display: flex; align-items: center; gap: 22px;
  }
  .brand-dot {
    flex: none; width: 34px; height: 34px; border-radius: 50%;
    background: var(--signal);
  }
  .brand-name {
    color: var(--ink); font-weight: 800; font-size: 54px;
    line-height: 1.02; text-transform: uppercase; letter-spacing: 2px;
  }
  .contact {
    position: absolute; right: 42px; top: 26px; text-align: right;
    color: var(--light-text);
  }
  .contact-phone {
    display: flex; align-items: center; justify-content: flex-end; gap: 18px;
    font-weight: 700; font-size: 50px; line-height: 1;
  }
  .contact-phone svg { width: 34px; height: 34px; }
  .contact-web {
    margin-top: 12px; font-weight: 500; font-size: 23px; letter-spacing: 2px;
  }
</style>
</head>
<body>
  <section class="backdrop">
    <svg class="backdrop-art" viewBox="0 0 1160 574" width="1160" height="574">
      <defs>
        <linearGradient id="team-fade" x1="0" x2="1" y1="0" y2="0">
          <stop offset="0" stop-color="#bdbdbd" stop-opacity="0"/>
          <stop offset="0.35" stop-color="#6a6a6a" stop-opacity="0.55"/>
          <stop offset="1" stop-color="#2e2e2e" stop-opacity="0.8"/>
        </linearGradient>
      </defs>
      <rect class="team-photo" x="508" y="115" width="652" height="300" fill="url(#team-fade)"
            role="img" aria-label="Photo of three smiling uniformed security officers in front of a building"/>
      <path class="accent-wave" fill="var(--signal)"
            d="M380,528 C560,498 720,300 900,304 C1020,307 1100,334 1160,350 L1160,382 C1100,362 1020,338 900,336 C700,332 520,530 330,550 Z"/>
      <path class="base-wave" fill="var(--night)"
            d="M0,434 C120,520 220,560 330,550 C520,530 700,332 900,336 C1020,338 1100,362 1160,382 L1160,574 L0,574 Z"/>
    </svg>

    <div class="brand-lockup">
      <span class="brand-dot"></span>
      <span class="brand-name">Keystone Ward Security</span>
    </div>

    <div class="contact">
      <div class="contact-phone">
        <svg viewBox="0 0 24 24" aria-hidden="true">
          <path fill="none" stroke="currentColor" stroke-width="2" stroke-linejoin="round"
                d="M6.5 3h3l1.5 4.5-2 1.5a11 11 0 0 0 6 6l1.5-2 4.5 1.5v3a2 2 0 0 1-2 2A17 17 0 0 1 4.5 5a2 2 0 0 1 2-2z"/>
          <path fill="none" stroke="currentColor" stroke-width="1.8" stroke-linecap="round"
                d="M14 6a4 4 0 0 1 4 4M14 2.5a7.5 7.5 0 0 1 7.5 7.5"/>
        </svg>
        <span>801.555.0142</span>
      </div>
      <div class="contact-web">www.KeystoneWardSecurity.com</div>
    </div>
  </section>
</body>
</html>
```